R. P. Pelsar & Associates, Inc

Rodrigo Pelsar
Accountant
4213 SE 87th AVE
Marlow Park, Florida 33099
(555) 482-0917
rod.pelsar@quillmail.net
Accounting - Tax Preparation Services - Bookkeeping
Side - one business logo on the left and business information on right
On Backside: The logo in the middle and under the logo my company name.

Rounded Corner of the cards
In reference to the logo and cards I need to adjust the circle around the RP and color.

```html
<!DOCTYPE html>
<html lang="en">
<head>
<meta charset="utf-8">
<title>R. P. Pelsar &amp; Associates, Inc — Business Cards</title>
<link rel="stylesheet" href="https://fonts.googleapis.com/css2?family=Red+Hat+Display:wght@400;500&display=swap">
<style>
  :root {
    --backdrop: #e4e4e4;
    --card-dark: #1f1c1d;
    --card-light: #f4f4f4;
    --accent-blue: #1a6fb8;
    --text-light: #ffffff;
    --text-dark: #1f1c1d;
  }
  * { margin: 0; padding: 0; box-sizing: border-box; }
  html, body {
    width: 1200px;
    height: 960px;
    overflow: hidden;
  }
  body {
    position: relative;
    background: var(--backdrop);
    font-family: "Red Hat Display", Arial, sans-serif;
  }
  .card {
    position: absolute;
    left: 303px;
    width: 598px;
    height: 341px;
    border-radius: 22px;
    overflow: hidden;
    background: var(--card-dark);
  }
  .card--back { top: 120px; }
  .card--front { top: 515px; }

  /* Back side */
  .brand-mark {
    position: absolute;
    left: 0;
    right: 0;
    top: 132px;
    display: flex;
    justify-content: center;
    align-items: center;
    gap: 12px;
    color: var(--text-light);
    font-size: 32px;
    font-weight: 500;
  }
  .brand-mark__dot {
    width: 14px;
    height: 14px;
    border-radius: 50%;
    background: var(--accent-blue);
  }
  .company-name {
    position: absolute;
    left: 0; right: 0;
    top: 252px;
    text-align: center;
    color: var(--text-light);
    font-size: 18.5px;
    font-weight: 500;
  }
  .services {
    position: absolute;
    left: 0; right: 0;
    top: 297px;
    text-align: center;
    color: var(--text-light);
    font-size: 16px;
    font-weight: 400;
  }
  .services__divider { color: var(--accent-blue); padding: 0 2px; }

  /* Front side */
  .front-shape {
    position: absolute;
    inset: 0;
    width: 598px;
    height: 341px;
  }
  .front-brand {
    position: absolute;
    left: 0;
    width: 262px;
    top: 152px;
    display: flex;
    justify-content: center;
    align-items: center;
    gap: 10px;
    color: var(--text-dark);
    font-size: 26px;
    font-weight: 500;
  }
  .front-brand__dot {
    width: 12px;
    height: 12px;
    border-radius: 50%;
    background: var(--accent-blue);
  }
  .contact {
    position: absolute;
    left: 308px;
    top: 97px;
    color: var(--text-light);
    font-size: 16px;
    line-height: 20px;
  }
  .contact__name {
    color: var(--accent-blue);
    font-size: 20px;
    font-weight: 500;
    line-height: 24px;
  }
  .contact__title { font-size: 15.5px; margin-bottom: 14px; }
  .contact__city { margin-bottom: 6px; }
  .contact__line {
    display: flex;
    align-items: center;
    gap: 6px;
  }
  .contact__icon { width: 14px; height: 14px; flex: none; }
</style>
</head>
<body>

  <section class="card card--back" aria-label="Business card back">
    <div class="brand-mark">
      <span class="brand-mark__dot"></span>
      <span>R. P. Pelsar</span>
    </div>
    <p class="company-name">R. P. Pelsar &amp; Associates, Inc</p>
    <p class="services">
      Accounting <span class="services__divider">|</span> Tax Preparation Services <span class="services__divider">|</span> Bookkeeping
    </p>
  </section>

  <section class="card card--front" aria-label="Business card front">
    <svg class="front-shape" viewBox="0 0 598 341" aria-hidden="true">
      <path d="M212 0 Q334 170.5 212 341 Z" fill="var(--accent-blue)"/>
      <path d="M0 0 H212 Q308 170.5 212 341 H0 Z" fill="var(--card-light)"/>
    </svg>

    <div class="front-brand">
      <span class="front-brand__dot"></span>
      <span>R. P. Pelsar</span>
    </div>

    <div class="contact">
      <p class="contact__name">Rodrigo Pelsar</p>
      <p class="contact__title">Accountant</p>
      <p>4213 SE 87th AVE</p>
      <p class="contact__city">Marlow Park, Florida 33099</p>
      <p class="contact__line">
        <svg class="contact__icon" viewBox="0 0 24 24" aria-hidden="true">
          <path fill="var(--accent-blue)" d="M6.6 10.8c1.4 2.8 3.8 5.1 6.6 6.6l2.2-2.2c.3-.3.7-.4 1-.2 1.1.4 2.3.6 3.6.6.6 0 1 .4 1 1V20c0 .6-.4 1-1 1C10.6 21 3 13.4 3 4c0-.6.4-1 1-1h3.5c.6 0 1 .4 1 1 0 1.3.2 2.5.6 3.6.1.3 0 .7-.2 1L6.6 10.8z"/>
        </svg>
        (555) 482-0917
      </p>
      <p class="contact__line">
        <svg class="contact__icon" viewBox="0 0 24 24" aria-hidden="true">
          <rect x="2.5" y="5" width="19" height="14" rx="1" fill="none" stroke="var(--accent-blue)" stroke-width="2"/>
          <path d="M3 6l9 7 9-7" fill="none" stroke="var(--accent-blue)" stroke-width="2"/>
        </svg>
        rod.pelsar@quillmail.net
      </p>
    </div>
  </section>

</body>
</html>
```